Exciting opportunity to create logo and a label for our natural health brand.

About us

We are a customer centric health supplement brand who believes in natural medicine and high quality ingredients. We take a holistic approach to healthcare, with an eastern philosophy. We believe in being partners with our customers in their health care journey and are invested in their well being.

Our brand philosophy and values are attached (see Varo philosophy.png). Our personality traits are:

- Natural
- Fresh
- Modern
- Balanced (in a holistic sense)

Task breakdown

1. Design a fresh feeling logo for us
- We want it to represent our values and high quality ingredients. We would like the quality of the product to be reflected in the branding and have a high end feel.
- Logo text must include Varo Health Sciences
- We want the Varo to be the focus of the logo (see uploaded image Varo logo example.png)
The logo does not have to follow this layout, but we just want the Varo to stand out. Feel free to use your creative license on this!

2. Create an attractive label to go on the supplement bottle
- The designs need to be eye catching, give a sense of high end ingredients and natural products and tie in with the logo to give a joined up feel.
- We are selling our products online and need them to really stand out from the competition.
- See examples of labels and packaging we like (1 -7 label design).

The initial label we would like you to design would be for our product Calm Haven. It is a product that assists in the management of Anxiety and stress. The label will appear on the bottle that holds the capsules for this supplement, see uploaded files (Example plain bottles.png). The bottles may be white as the picture shows or dark blue recyclable plastic or dark brown glass . We don't have the exact dimensions of the bottle yet, but I will follow up with these.

The label needs to include the following things:
1. The logo
2. The name of the product
3. The product is to help with the relief of Anxiety and Stress
4. Number of capsules the bottle contains
5. The back of the label should have
i) The ingredients
ii) Dosage
iii) Directions of use

Please use placeholder text where needed.

We look forward to seeing your design. Thank you.

```html
<!DOCTYPE html>
<html lang="en">
<head>
<meta charset="utf-8">
<title>Varo Health Sciences – Identity and Calm Haven Label</title>
<link rel="stylesheet" href="https://fonts.googleapis.com/css2?family=Maven+Pro:wght@400;500;600;700&display=swap">
<style>
  :root {
    --lime: #8dc63f;
    --forest: #0b6b3a;
    --sun: #fdc010;
    --ink: #231f20;
    --body: #4d4d4f;
    --stage: #939598;
    --paper: #ffffff;
  }
  * { margin: 0; padding: 0; box-sizing: border-box; }
  html, body { width: 1200px; height: 1200px; overflow: hidden; background: var(--paper); }
  body { font-family: "Maven Pro", sans-serif; color: var(--ink); position: relative; }

  .wordmark { position: absolute; left: 0; width: 1200px; text-align: center; }
  .wordmark-primary { top: 95px; }
  .wordmark-primary .brand-name {
    display: block; font-size: 250px; font-weight: 700; line-height: 250px;
    color: var(--lime); letter-spacing: -4px;
  }
  .wordmark-primary .brand-tagline {
    display: block; margin-top: 8px; font-size: 38px; font-weight: 500;
    letter-spacing: 0.22em; color: var(--forest);
  }

  .wordmark-inline { top: 500px; display: flex; justify-content: center; align-items: baseline; gap: 22px; }
  .wordmark-inline .brand-name { font-size: 82px; font-weight: 700; color: var(--lime); line-height: 1; }
  .wordmark-inline .brand-tagline { font-size: 34px; font-weight: 500; letter-spacing: 0.24em; color: var(--forest); }

  .label-stage { position: absolute; left: 12px; top: 660px; width: 1176px; height: 528px; background: var(--stage); }

  .label-sheet { position: absolute; left: 0; top: 0; width: 1200px; height: 1200px; }

  .text-block { position: absolute; font-size: 11px; line-height: 17px; color: var(--body); text-align: justify; }
  .text-block strong { color: var(--ink); font-weight: 600; }

  .product-mark { position: absolute; background: var(--sun); border-radius: 50%; }

  .back-title { position: absolute; left: 312px; top: 759px; font-size: 16px; font-weight: 600; color: var(--ink); }
  .back-directions {
    left: 276px; top: 792px; width: 176px; height: 140px;
    font-size: 10px; line-height: 14.5px; overflow: hidden;
  }

  .band { position: absolute; top: 940px; height: 30px; background: var(--forest); display: flex; align-items: center; }
  .band-back { left: 250px; width: 226px; padding-left: 24px; gap: 8px; }
  .band-back .band-brand { font-size: 15px; font-weight: 600; color: var(--paper); letter-spacing: 0.12em; }
  .band-front { left: 726px; width: 226px; justify-content: center; }
  .band-front span { font-size: 12px; font-weight: 500; color: var(--paper); letter-spacing: 0.08em; }

  .distributor { left: 276px; top: 984px; width: 174px; font-size: 7.5px; line-height: 11px; }

  .description { left: 492px; top: 832px; width: 222px; font-size: 12px; line-height: 18px; }

  .ingredients-box {
    position: absolute; left: 474px; top: 920px; width: 255px; height: 56px;
    background: var(--paper); border: 2px solid var(--forest); padding: 6px 14px;
  }
  .ingredients-box p { font-size: 8.5px; line-height: 12px; color: var(--body); text-align: justify; }
  .ingredients-box strong { color: var(--ink); font-weight: 600; }

  .front-brand { position: absolute; left: 726px; width: 226px; top: 748px; text-align: center; color: var(--lime); font-weight: 700; }
  .front-brand .brand-name { display: block; font-size: 40px; line-height: 40px; }
  .front-brand .brand-tagline { display: block; font-size: 9px; letter-spacing: 0.1em; margin-top: 2px; }

  .front-title { position: absolute; left: 726px; width: 226px; top: 887px; text-align: center; font-size: 25px; font-weight: 500; color: var(--ink); }

  .count-box {
    position: absolute; left: 814px; top: 987px; width: 50px; height: 45px; background: var(--lime);
    color: var(--paper); font-size: 28px; font-weight: 600; display: flex; align-items: center; justify-content: center;
  }
  .count-unit { position: absolute; left: 726px; width: 226px; top: 1040px; text-align: center; font-size: 10px; color: var(--forest); }

  .panel-caption { position: absolute; top: 1096px; font-size: 24px; font-weight: 500; color: var(--ink); text-align: center; width: 226px; }
  .caption-back { left: 250px; }
  .caption-front { left: 726px; }
</style>
</head>
<body>

  <div class="wordmark wordmark-primary">
    <span class="brand-name">Varo</span>
    <span class="brand-tagline">health sciences</span>
  </div>

  <div class="wordmark wordmark-inline">
    <span class="brand-name">Varo</span>
    <span class="brand-tagline">health sciences</span>
  </div>

  <div class="label-stage"></div>

  <svg class="label-sheet" viewBox="0 0 1200 1200" aria-hidden="true">
    <defs>
      <filter id="label-shadow" x="-10%" y="-10%" width="120%" height="120%">
        <feDropShadow dx="0" dy="3" stdDeviation="4" flood-color="#000" flood-opacity="0.35"/>
      </filter>
    </defs>
    <path fill="#ffffff" filter="url(#label-shadow)"
      d="M272 732 H454 A22 22 0 0 1 476 754 V796 A22 22 0 0 0 498 818 H704 A22 22 0 0 0 726 796 V754 A22 22 0 0 1 748 732 H930 A22 22 0 0 1 952 754 V1050 A22 22 0 0 1 930 1072 H748 A22 22 0 0 1 726 1050 V1012 A22 22 0 0 0 704 990 H498 A22 22 0 0 0 476 1012 V1050 A22 22 0 0 1 454 1072 H272 A22 22 0 0 1 250 1050 V754 A22 22 0 0 1 272 732 Z"/>
  </svg>

  <!-- Back panel -->
  <span class="product-mark" style="left:276px; top:754px; width:24px; height:24px;"></span>
  <h2 class="back-title">Calm Haven</h2>
  <p class="text-block back-directions"><strong>Dosage and direction of use</strong> Lorem ipsum dolor sit amet, consectetuer adipiscing elit, sed diam nonummy nibh euismod tincidunt ut laoreet dolore magna. Lorem ipsum dolor sit amet, consectetuer adipiscing elit, sed diam nonummy nibh euismod tincidunt ut laoreet dolore magna.</p>

  <div class="band band-back"><span class="band-brand">Varo health sciences</span></div>

  <p class="text-block distributor"><strong>Distributor information</strong> Distributed by Varo Health Sciences Ltd. Store in a cool dry place away from direct sunlight. Keep out of reach of children. Do not exceed the stated daily dose.</p>

  <!-- Spine -->
  <p class="text-block description"><strong>Desription</strong> Lorem ipsum dolor sit amet, consectetuer adipiscing elit, sed diam nonummy nibh euismod tincidunt ut laoreet dolore magna.</p>

  <div class="ingredients-box">
    <p><strong>Ingredients</strong> Lorem ipsum dolor sit amet, consectetuer adipiscing elit, sed diam nonummy nibh euismod tincidunt ut laoreet dolore magna.</p>
  </div>

  <!-- Front panel -->
  <div class="front-brand">
    <span class="brand-name">Varo</span>
    <span class="brand-tagline">health sciences</span>
  </div>
  <span class="product-mark" style="left:824px; top:842px; width:30px; height:30px;"></span>
  <h1 class="front-title">Calm Haven</h1>
  <div class="band band-front"><span>Anxiety And Stress Relief</span></div>
  <div class="count-box">50</div>
  <span class="count-unit">capsules</span>

  <span class="panel-caption caption-back">back cover</span>
  <span class="panel-caption caption-front">Cover</span>

</body>
</html>
```